Fun, easy to read post card design

Brindle Networks is looking for a designer to create a new (within theme) postcard design.

We have new internet packages rolling out and need to advertise it. Attached is a snippet from our website displaying those new internet plans, our logo and font.

https://www.brindlenetworks.ca/residential/

We would like the focus phrase to be "Fast, local reliable internet"

Let's see what you can come up with!

```html
<!DOCTYPE html>
<html lang="en">
<head>
<meta charset="utf-8">
<title>Brindle Networks Postcard</title>
<link href="https://fonts.googleapis.com/css2?family=Lato:wght@400;700&family=Montserrat:ital,wght@0,600;0,800;0,900;1,900&display=swap" rel="stylesheet">
<style>
  :root{
    --blue:#1596d8;
    --blue-bright:#1ab0ea;
    --blue-deep:#17709f;
    --charcoal:#2c2d30;
    --panel:#3b3c40;
    --paper:#eceef0;
    --white:#ffffff;
    --page:#dcdde0;
  }
  *{box-sizing:border-box;margin:0;padding:0}
  html,body{width:1200px;height:1029px;overflow:hidden;background:var(--page);font-family:'Lato',sans-serif}
  .postcard{position:absolute;left:220px;width:760px;height:486px;overflow:hidden;box-shadow:0 6px 18px rgba(0,0,0,.18)}
  .front{top:18px;background:var(--paper)}
  .back{top:524px;background:var(--white)}

  /* front */
  .brand-panel{position:absolute;left:0;top:0;width:340px;height:150px;background:linear-gradient(135deg,#1a82bd,var(--blue-deep));clip-path:polygon(0 0,100% 0,80% 100%,0 100%)}
  .brand-mark{position:absolute;left:52px;top:18px;width:104px;height:104px;border-radius:50%;background:var(--white)}
  .brand-name{position:absolute;left:22px;top:150px;font-family:'Montserrat',sans-serif;font-weight:600;font-size:25px;color:var(--blue)}
  .hero-photo{position:absolute;left:250px;top:22px;width:510px;height:168px;background:linear-gradient(100deg,#4a3a30,#2a2420 45%,#151518);clip-path:polygon(13% 0,100% 0,100% 100%,0 100%)}
  .headline{position:absolute;right:22px;top:40px;text-align:right;font-family:'Montserrat',sans-serif;font-weight:900;font-style:italic;font-size:23px;line-height:1.12;text-transform:uppercase}
  .headline .b{color:var(--blue)}
  .headline .w{color:var(--white)}
  .signup-band{position:absolute;left:0;top:300px;width:760px;height:186px;background:var(--charcoal)}
  .plans{position:absolute;left:30px;top:206px;display:flex;gap:9px}
  .plan{width:133px;height:160px;background:var(--panel);color:var(--white);text-align:center}
  .plan-name{height:36px;line-height:36px;background:linear-gradient(90deg,var(--blue-deep),var(--blue-bright));font-size:16px;font-weight:700;letter-spacing:.5px}
  .plan-specs{margin:8px 8px 0;border-top:1px solid #8a8b90;border-bottom:1px solid #8a8b90;padding:6px 0;font-size:9.5px;line-height:1.45}
  .plan-specs strong{display:block;font-weight:700}
  .plan-price{padding-top:7px;font-size:10px;line-height:1.3}
  .plan-price strong{font-size:11px}
  .cta{position:absolute;left:0;width:760px;top:392px;text-align:center;font-family:'Montserrat',sans-serif;font-weight:900;color:var(--blue-bright);font-size:34px;line-height:1.12;text-transform:uppercase}

  /* back */
  .info-side{position:absolute;left:0;top:0;width:470px;height:486px;background:linear-gradient(135deg,#2d2e31,#202124);padding:30px 32px;color:var(--white)}
  .divider{position:absolute;left:470px;top:0;width:7px;height:486px;background:var(--blue)}
  .offer{font-family:'Montserrat',sans-serif;font-weight:900;font-style:italic;color:var(--blue);font-size:30px;line-height:1.08;text-transform:uppercase}
  .rule{height:3px;background:var(--blue);margin:10px 0 12px;width:320px}
  .info-title{font-family:'Montserrat',sans-serif;font-weight:800;color:var(--blue);font-size:16px;margin:6px 0 5px}
  .info-text{font-size:10.5px;line-height:1.4}
  .info-list{margin:3px 0 8px 16px;font-size:10.5px;line-height:1.4}
  .toll{margin-top:22px;font-family:'Montserrat',sans-serif;font-weight:900;font-style:italic;color:var(--blue);font-size:34px;line-height:1.1}
  .address-line{position:absolute;left:540px;width:190px;height:1px;background:#9a9b9f}
</style>
</head>
<body>

<section class="postcard front">
  <div class="hero-photo" role="img" aria-label="Family cheering while watching a football match on TV in a living room"></div>
  <div class="brand-panel"><div class="brand-mark"></div></div>
  <div class="brand-name">Brindle Networks</div>
  <h1 class="headline">
    <span class="b">Keep</span><br><span class="w">Connected</span><br><span class="b">To What</span><br><span class="w">Matters</span><br><span class="b">Most</span>
  </h1>
  <div class="signup-band"></div>
  <div class="plans">
    <div class="plan"><div class="plan-name">SILVER</div><div class="plan-specs">Download Speed<strong>10 Mbps</strong>Upload Speed<strong>2 Mbps</strong>Monthly Data<strong>250GB</strong></div><div class="plan-price"><strong>$69.95</strong><br>per month</div></div>
    <div class="plan"><div class="plan-name">GOLD</div><div class="plan-specs">Download Speed<strong>20 Mbps</strong>Upload Speed<strong>3 Mbps</strong>Monthly Data<strong>500GB</strong></div><div class="plan-price"><strong>$79.95</strong><br>per month</div></div>
    <div class="plan"><div class="plan-name">PLATINUM</div><div class="plan-specs">Download Speed<strong>30 Mbps</strong>Upload Speed<strong>4 Mbps</strong>Monthly Data<strong>1000GB</strong></div><div class="plan-price"><strong>$94.95</strong><br>per month</div></div>
    <div class="plan"><div class="plan-name">ADVANCE</div><div class="plan-specs">Download Speed<strong>35 Mbps</strong>Upload Speed<strong>5 Mbps</strong>Monthly Data<strong>1200GB</strong></div><div class="plan-price"><strong>$99.95</strong><br>per month</div></div>
    <div class="plan"><div class="plan-name">UNLIMITED</div><div class="plan-specs">Download Speed<strong>35 Mbps</strong>Upload Speed<strong>5 Mbps</strong>Monthly Data<strong>UnlimitedGB</strong></div><div class="plan-price"><strong>$149.95</strong><br>per month</div></div>
  </div>
  <p class="cta">Sign Up Today<br>Or Call 1-780-555-0148</p>
</section>

<section class="postcard back">
  <div class="info-side">
    <h2 class="offer">Free Install!<br>No Contracts!</h2>
    <div class="rule"></div>
    <h3 class="info-title">Why Choose Brindle Networks?</h3>
    <p class="info-text">What sets Brindle Networks apart:</p>
    <ul class="info-list">
      <li>Fast, local, reliable, internet access for your home</li>
      <li>You will get the speed you are paying for! No up to speeds, or prime time slowdowns!</li>
      <li>Great customer care for Alberta and Saskatchewan</li>
      <li>Multiple or customizable plan options to suit your needs and your budget</li>
    </ul>
    <h3 class="info-title">What monthly traffic/speed do I need?</h3>
    <p class="info-text">If you do only basic internet browsing and don't spend much time on your computer, you should choose the silver plan. If you're on your computer often and use email, social media, video streaming and downloading services, such as Streamly and TuneBox, you should choose gold or platinum. If you have multiple internet users in your household who stream videos and play online video games, you should choose platinum or advanced.</p>
    <div class="rule"></div>
    <p class="toll">Toll Free:<br>1-866-555-0192</p>
  </div>
  <div class="divider"></div>
  <div class="address-line" style="top:300px"></div>
  <div class="address-line" style="top:345px"></div>
  <div class="address-line" style="top:390px"></div>
</section>

</body>
</html>
```